New Website for novelty yarn producer

We need a new website for our company, Merovac. We make highly tailored yarns for weavers worldwide. This year marks our 40th anniversary and we want to evolve our image and identity.

Our temporary website can be found at:
www.merovacyarns-example.com

Our only concern in that throughout the website the protagonist must be our client, we make their creations possible and are highly adaptable both during the ideation process of the yarn as well as in the production. This is at the core of the way we do business and is summarised within the concept of OBM (Open Bridge Method).

Industry/Entity Type

Textile

Number of Pages Required

1 page

Colors
9bcb3c

Requirements
Must have
• Open Bridge Method (OBM) - can be found on or current website www.merovacyarns-example.com

```html
<!DOCTYPE html>
<html lang="en">
<head>
<meta charset="utf-8">
<title>Merovac — Tailored Weaving Solutions</title>
<link rel="stylesheet" href="https://fonts.googleapis.com/css2?family=Merriweather:wght@400;700&family=Lato:wght@400;700&display=swap">
<style>
:root{
  --green:#5cb54a;
  --green-soft:#9bcb3c;
  --ink:#2b2b2b;
  --text:#555;
  --muted:#888;
  --line:#e3e3e3;
  --grey-band:#f1f1f1;
  --dark:#262626;
  --darker:#1c1c1c;
  --white:#fff;
}
*{box-sizing:border-box;margin:0;padding:0}
html,body{width:1200px;height:3648px;overflow:hidden;background:var(--white)}
body{font-family:"Lato",sans-serif;color:var(--text);font-size:14px;line-height:1.5}
a{color:inherit;text-decoration:none}
.btn{display:inline-block;border:2px solid var(--green);color:var(--ink);background:var(--white);font-size:14px;padding:8px 22px}
.btn.light{border-color:var(--white);color:var(--white);background:transparent}
.section-title{font-family:"Merriweather",serif;font-weight:700;color:var(--ink);font-size:32px;text-align:center}

/* header */
.site-header{height:140px;position:relative;display:flex;align-items:center;justify-content:center}
.brand{font-family:"Merriweather",serif;font-weight:700;font-size:40px;letter-spacing:4px;color:var(--ink)}
.menu-toggle{position:absolute;right:100px;top:58px;width:26px}
.menu-toggle span{display:block;height:4px;background:var(--green);margin-bottom:5px}

/* hero */
.hero{position:relative;height:648px;background:linear-gradient(160deg,#3a2a2e 0%,#7c3840 30%,#4a3c4c 55%,#8a4a3a 75%,#3b2f33 100%);color:var(--white);text-align:center}
.hero::after{content:"";position:absolute;inset:0;background:rgba(0,0,0,.28)}
.hero-content{position:relative;z-index:1;padding-top:196px}
.badge-40{width:128px;height:128px;border:3px solid var(--white);border-radius:50%;margin:0 auto;display:flex;flex-direction:column;align-items:center;justify-content:center}
.badge-40 strong{font-family:"Merriweather",serif;font-size:46px;line-height:1;font-weight:400}
.badge-40 small{font-size:14px;letter-spacing:2px}
.hero h1{font-family:"Merriweather",serif;font-size:32px;margin-top:24px}
.hero p{width:300px;margin:6px auto 16px;font-size:15px;line-height:1.35}
.hero .btn{background:transparent;color:var(--white);border-color:var(--white)}
.slide-arrow{position:absolute;z-index:1;top:310px;width:30px;height:30px;background:var(--white);display:flex;align-items:center;justify-content:center}
.slide-arrow.prev{left:34px}.slide-arrow.next{right:34px}

/* features */
.features{height:412px;display:flex;justify-content:center;gap:32px;padding-top:64px}
.feature{width:296px;height:240px;text-align:center;padding-top:36px}
.feature h3{font-family:"Merriweather",serif;font-size:26px;color:var(--ink);margin-top:10px}
.feature p{width:210px;margin:6px auto 4px;font-size:14px;line-height:1.3}
.feature .more{font-size:13px;color:var(--ink)}
.feature.active{background:var(--green);color:var(--white);height:300px}
.feature.active h3,.feature.active .more{color:var(--white)}

/* method */
.method{position:relative;height:440px;background:var(--grey-band);overflow:hidden}
.yarn-photo{position:absolute}
.yarn-a{left:0;top:0;width:260px;height:150px;background:linear-gradient(100deg,#d9a2c0,#9c8fc8 50%,rgba(241,241,241,0))}
.yarn-b{right:0;bottom:0;width:300px;height:150px;background:linear-gradient(280deg,#e85a9a,#4568c9 50%,rgba(241,241,241,0))}
.method-name{position:absolute;left:170px;top:160px;font-family:"Lato",sans-serif;font-size:30px;line-height:1.25;color:#666;letter-spacing:2px}
.method-text{position:absolute;left:600px;top:134px;width:420px}
.method-text h2{font-family:"Merriweather",serif;font-size:24px;color:var(--ink)}
.method-text h2 span{color:var(--green)}
.method-text p{font-size:13px;line-height:1.45;margin:14px 0 20px}

/* heritage */
.heritage{height:420px;text-align:center;padding-top:90px}
.heritage p{width:560px;margin:24px auto 0;font-size:13px;line-height:1.5}
.heritage p+p{margin-top:14px}
.heritage .btn{margin-top:30px}

/* numbers */
.numbers{position:relative;height:440px;background:linear-gradient(135deg,#3c2d2a,#5a4034 40%,#2f2a2a 70%,#4a3a36);color:var(--white);text-align:center}
.numbers::after{content:"";position:absolute;inset:0;background:rgba(0,0,0,.35)}
.numbers-inner{position:relative;z-index:1;padding-top:80px}
.numbers h2{font-family:"Merriweather",serif;font-size:28px;line-height:1.35;font-weight:700}
.stats{display:flex;justify-content:center;gap:170px;margin-top:28px}
.stat .circle{width:84px;height:84px;border-radius:50%;background:var(--green);margin:0 auto;display:flex;align-items:center;justify-content:center;font-family:"Merriweather",serif;font-size:32px;font-weight:700}
.stat span{display:block;margin-top:12px;font-size:15px}
.numbers .btn{margin-top:24px;padding:6px 20px}

/* blog */
.blog{height:572px;background:#f6f6f6;padding-top:36px;text-align:center}
.blog .lead{font-size:15px;color:var(--ink);margin-top:2px}
.cards{display:flex;justify-content:center;gap:32px;margin-top:20px}
.card{width:296px;height:320px;background:var(--white);text-align:left;border:1px solid var(--line)}
.card .thumb{position:relative;height:188px}
.thumb.spools{background:linear-gradient(180deg,#d8d8d8,#6e6e6e 55%,#3a3a3a)}
.thumb.wall{background:linear-gradient(160deg,#a9a08a,#6d8a6d 45%,#5f5a4a)}
.thumb.balls{background:linear-gradient(150deg,#e8e4dc,#5eb2ad 45%,#2f7e86)}
.date-tag{position:absolute;left:14px;top:14px;background:var(--green);color:var(--white);font-size:11px;line-height:1.1;text-align:center;padding:6px 8px;font-weight:700}
.card-body{padding:14px 18px}
.card h4{font-size:13px;color:var(--ink);font-weight:700}
.meta{display:flex;justify-content:space-between;font-size:11px;color:var(--muted);margin:4px 0 6px}
.meta .date{color:var(--green)}
.card p{font-size:13px;line-height:1.35}
.card .more{font-size:13px;color:var(--ink);font-weight:700}
.card.featured{background:var(--green);color:var(--white);border-color:var(--green)}
.card.featured h4,.card.featured .more,.card.featured .meta,.card.featured .meta .date{color:var(--white)}
.blog .btn{margin-top:34px;padding:7px 22px}

/* newsletter */
.newsletter{height:180px;text-align:center;padding-top:34px}
.newsletter h2{font-family:"Merriweather",serif;font-size:26px;color:var(--ink)}
.subscribe{display:flex;justify-content:center;margin-top:22px}
.subscribe .field{width:330px;height:34px;border:1px solid #ccc;text-align:left;padding:7px 12px;color:#aaa;font-size:13px}
.subscribe .send{width:110px;height:34px;background:var(--green);color:var(--white);font-weight:700;font-size:13px;display:flex;align-items:center;justify-content:center}

/* footer */
.site-footer{height:348px;background:linear-gradient(160deg,var(--dark),var(--darker));color:#ccc;position:relative;padding:76px 0 0 120px;display:flex}
.foot-col h5{color:var(--white);font-size:15px;letter-spacing:1px;margin-bottom:16px}
.foot-about{width:260px;padding-right:30px}
.foot-about .brand{color:var(--white);font-size:30px;letter-spacing:3px}
.foot-about p{font-size:13px;line-height:1.4;margin-top:12px}
.foot-about .more{color:var(--white);font-weight:700;font-size:13px;margin-top:8px;display:block}
.foot-links{width:180px}
.foot-links li{list-style:none;font-size:13px;line-height:1.55}
.foot-links li::before{content:"›";color:var(--green);margin-right:6px}
.foot-address{width:220px}
.foot-address li{list-style:none;display:flex;gap:10px;font-size:13px;margin-bottom:10px;align-items:flex-start}
.foot-contact{width:300px}
.contact-row{display:flex;gap:10px;margin-bottom:10px}
.contact-row div,.contact-msg{background:var(--white);color:#999;font-size:12px;padding:6px 10px;height:30px;flex:1}
.contact-msg{height:56px}
.contact-send{margin:12px 0 0 auto;width:90px;height:28px;background:var(--green);color:var(--white);font-size:12px;font-weight:700;display:flex;align-items:center;justify-content:center;border-radius:3px}
.social{position:absolute;right:120px;top:30px;display:flex;gap:8px}
.social i{display:block;width:24px;height:24px;border-radius:50%;background:var(--white)}
.social i:first-child{background:var(--green)}
.bottom-bar{height:48px;display:flex;align-items:center;justify-content:space-between;padding:0 120px;font-size:13px;color:var(--ink);font-weight:700}
.bottom-bar .social{position:static}
.bottom-bar .social i{background:var(--ink)}
.bottom-bar .social i:first-child{background:var(--green)}
</style>
</head>
<body>

<header class="site-header">
  <a class="brand" href="#">MEROVAC</a>
  <div class="menu-toggle" aria-label="Menu"><span></span><span></span><span></span></div>
</header>

<section class="hero" role="img" aria-label="Close-up photograph of woven yarn fabric in deep red and purple tones">
  <div class="hero-content">
    <div class="badge-40"><strong>40</strong><small>YEARS</small></div>
    <h1>Tailored Weaving Solutions</h1>
    <p>Lorem Ipsum is simply dummy text of the printing and typesetting.</p>
    <a class="btn" href="#">Read More</a>
  </div>
  <div class="slide-arrow prev"><svg width="10" height="12" viewBox="0 0 10 12"><path d="M8 1 2 6l6 5" fill="none" stroke="#333" stroke-width="2"/></svg></div>
  <div class="slide-arrow next"><svg width="10" height="12" viewBox="0 0 10 12"><path d="M2 1l6 5-6 5" fill="none" stroke="#333" stroke-width="2"/></svg></div>
</section>

<section class="features">
  <article class="feature">
    <svg width="46" height="46" viewBox="0 0 46 46" fill="none" stroke="#333" stroke-width="2.5"><rect x="5" y="14" width="36" height="26" rx="3"/><path d="M17 14V9h12v5M5 25h36"/></svg>
    <h3>Experience</h3>
    <p>Lorem Ipsum is simply dummy text of the printing and typesetting.</p>
    <a class="more" href="#">Read More ›</a>
  </article>
  <article class="feature active">
    <svg width="46" height="46" viewBox="0 0 46 46" fill="none" stroke="#fff" stroke-width="2.5"><path d="M23 10a11 11 0 0 0-6 20v5h12v-5a11 11 0 0 0-6-20zM18 39h10M23 2v4M8 8l3 3M38 8l-3 3M3 21h4M39 21h4"/></svg>
    <h3>Creativity</h3>
    <p>Lorem Ipsum is simply dummy text of the printing and typesetting.</p>
    <a class="more" href="#">Read More ›</a>
  </article>
  <article class="feature">
    <svg width="46" height="46" viewBox="0 0 46 46" fill="none" stroke="#333" stroke-width="2.5"><circle cx="23" cy="14" r="8"/><path d="M9 42c0-9 6-14 14-14s14 5 14 14M23 28v8"/></svg>
    <h3>Professionality</h3>
    <p>Lorem Ipsum is simply dummy text of the printing and typesetting.</p>
    <a class="more" href="#">Read More ›</a>
  </article>
</section>

<section class="method">
  <div class="yarn-photo yarn-a" role="img" aria-label="Photograph of colourful yarn balls"></div>
  <div class="yarn-photo yarn-b" role="img" aria-label="Photograph of colourful yarn balls"></div>
  <div class="method-name">OPEN<br>BRIDGE<br>METHOD</div>
  <div class="method-text">
    <h2><span>MRVC</span> Open Bridge Method</h2>
    <p>We believe that the key to delivering a yarn that exceeds our client's expectation is to work together with weavers from step one, starting from the desired end product and working backwards. This allows us to develop the product we are manufacturing, rather than having weavers adapt to the supplied raw materials.</p>
    <a class="btn" href="#">Read More</a>
  </div>
</section>

<section class="heritage">
  <h2 class="section-title">Our Heritage</h2>
  <p>Our team has decades of experience in providing yarn solutions to weavers around the world, assisting them in the creation of outstanding textiles.</p>
  <p>Our clients can expect open lines of communication, clarity and professionalism.</p>
  <p>Our focus is our client.<br>The success of a client is our success.</p>
  <a class="btn" href="#">Read More</a>
</section>

<section class="numbers" role="img" aria-label="Photograph of yarn cones in a mill, darkened">
  <div class="numbers-inner">
    <h2>MRV in Numbers<br>2017</h2>
    <div class="stats">
      <div class="stat"><div class="circle">40</div><span>Years in Business</span></div>
      <div class="stat"><div class="circle">2</div><span>Million Kilograms Yr</span></div>
      <div class="stat"><div class="circle">8</div><span>Brands</span></div>
    </div>
    <a class="btn light" href="#">Find More</a>
  </div>
</section>

<section class="blog">
  <h2 class="section-title">Our Blogs</h2>
  <p class="lead">Lorem Ipsum is simply dummy text.</p>
  <div class="cards">
    <article class="card">
      <div class="thumb spools" role="img" aria-label="Photograph of yarn spools on a machine"><div class="date-tag">03<br>MAR</div></div>
      <div class="card-body">
        <h4>BLOG POST TITLE</h4>
        <div class="meta"><span class="date">◷ March22, 2018</span><span>♡ 16 &nbsp; ▢ 12</span></div>
        <p>Lorem Ipsum is simply dummy text of the printing and typesetting industry.</p>
        <a class="more" href="#">Read More ›</a>
      </div>
    </article>
    <article class="card featured">
      <div class="thumb wall" role="img" aria-label="Photograph of a wall of fabric swatches"><div class="date-tag">03<br>MAR</div></div>
      <div class="card-body">
        <h4>BLOG POST TITLE</h4>
        <div class="meta"><span class="date">◷ March22, 2018</span><span>♡ 16 &nbsp; ▢ 12</span></div>
        <p>Lorem Ipsum is simply dummy text of the printing and typesetting industry.</p>
        <a class="more" href="#">Read More ›</a>
      </div>
    </article>
    <article class="card">
      <div class="thumb balls" role="img" aria-label="Photograph of teal yarn balls"><div class="date-tag">03<br>MAR</div></div>
      <div class="card-body">
        <h4>BLOG POST TITLE</h4>
        <div class="meta"><span class="date">◷ March22, 2018</span><span>♡ 16 &nbsp; ▢ 12</span></div>
        <p>Lorem Ipsum is simply dummy text of the printing and typesetting industry.</p>
        <a class="more" href="#">Read More ›</a>
      </div>
    </article>
  </div>
  <a class="btn" href="#">View More</a>
</section>

<section class="newsletter">
  <h2>Subscribe To Our Newsletter</h2>
  <div class="subscribe"><div class="field">Your E-Mail</div><div class="send">SUBMIT</div></div>
</section>

<footer class="site-footer">
  <div class="social"><i></i><i></i><i></i><i></i><i></i></div>
  <div class="foot-col foot-about">
    <div class="brand">MEROVAC</div>
    <p>Lorem Ipsum is simply dummy text of the printing and typesetting industry. Lorem Ipsum has been the industry's standard.</p>
    <a class="more" href="#">Read More ›</a>
  </div>
  <div class="foot-col foot-links">
    <h5>QUICK LINK</h5>
    <ul><li>Home</li><li>About us</li><li>Open Bridge</li><li>Heritage</li><li>Team</li><li>Blog</li><li>Contact</li></ul>
  </div>
  <div class="foot-col foot-address">
    <h5>ADDRESS</h5>
    <ul>
      <li><svg width="12" height="16" viewBox="0 0 12 16"><path d="M6 0a6 6 0 0 0-6 6c0 4 6 10 6 10s6-6 6-10a6 6 0 0 0-6-6z" fill="#5cb54a"/></svg><span>Via dei Telai 12<br>50100 Firenze - Italy</span></li>
      <li><svg width="14" height="14" viewBox="0 0 14 14"><path d="M3 1l3 3-2 2a8 8 0 0 0 4 4l2-2 3 3-2 2C6 13 1 8 1 3z" fill="#5cb54a"/></svg><span>+39 055 000 1111</span></li>
      <li><svg width="14" height="14" viewBox="0 0 14 14"><path d="M3 1l3 3-2 2a8 8 0 0 0 4 4l2-2 3 3-2 2C6 13 1 8 1 3z" fill="#5cb54a"/></svg><span>+39 055 000 2222</span></li>
      <li><svg width="14" height="12" viewBox="0 0 14 12"><rect x="0.5" y="0.5" width="13" height="11" fill="none" stroke="#5cb54a"/><path d="M1 1l6 5 6-5" fill="none" stroke="#5cb54a"/></svg><span>info@merovac-example.com</span></li>
    </ul>
  </div>
  <div class="foot-col foot-contact">
    <h5>QUICK CONTACT</h5>
    <div class="contact-row"><div>Name</div><div>Phone</div></div>
    <div class="contact-msg">Message</div>
    <div class="contact-send">SEND</div>
  </div>
</footer>

<div class="bottom-bar">
  <span>Copyright © 2018 MEROVAC. All Rights Reserved.</span>
  <div class="social"><i></i><i></i><i></i><i></i><i></i></div>
</div>

</body>
</html>
```